Broschüre im Bereich Steuerberatung
Zielgruppe
Steuerberatung
Aufgabenstellung
Die Seite 1 wäre eigentlich fertig, natürlich bin ich offen für Optimierungen. Die weiteren fünf Seiten gilt es noch zu gestalten:
Seite 1
Buchhaltung
Lohnwesen
Steuern
Firmengründung
Kontakt

```html
<!DOCTYPE html>
<html lang="de">
<head>
<meta charset="utf-8">
<title>Varen Treuhand – Broschüre</title>
<link href="https://fonts.googleapis.com/css2?family=Oswald:wght@400&family=Source+Serif+4:wght@400&family=Mulish:wght@400;800&display=swap" rel="stylesheet">
<style>
:root{
  --bg:#d9d9d3;
  --paper:#ffffff;
  --navy:#1f3f8a;
  --orange:#e8661e;
  --green:#9bb13c;
  --text:#333;
}
*{margin:0;padding:0;box-sizing:border-box}
html,body{width:1114px;height:1200px;overflow:hidden;background:var(--bg)}
body{position:relative;font-family:"Mulish",sans-serif;color:var(--text)}
.page{position:absolute;width:468px;height:331px;background:var(--paper)}
.col-l{left:60px}.col-r{left:573px}
.row1{top:58px}.row2{top:430px}.row3{top:804px}
.kicker{position:absolute;left:20px;top:38px;font-family:"Oswald",sans-serif;font-size:12px;letter-spacing:3px;color:var(--navy);white-space:nowrap}
.kicker .sep{display:inline-block;width:5px;height:9px;background:var(--orange);margin:0 4px 0 1px;vertical-align:-1px}
.photo{position:absolute;left:20px;top:67px;width:223px;height:223px;background:linear-gradient(135deg,#c99f84 0%,#9aa06c 45%,#5f84a8 100%)}
.photo.warm{background:linear-gradient(135deg,#d49a6c 0%,#a8a25a 40%,#6c8cb4 100%)}
.photo.hands{background:linear-gradient(135deg,#c97a4c 0%,#b7896c 50%,#8a92a8 100%)}
.photo-word{position:absolute;font-family:"Source Serif 4",serif;color:#fff;line-height:.85;text-align:right}
.brand-name{position:absolute;left:16px;top:18px;font-family:"Mulish",sans-serif;font-weight:800;font-size:15px;line-height:1;color:#fff}
.photo-url{position:absolute;left:132px;top:203px;font-size:7px;font-weight:800;color:var(--orange)}
.head{position:absolute;left:253px;width:205px;font-weight:800;font-size:7.2px;line-height:9.4px;color:var(--navy)}
.sub{position:absolute;left:253px;width:205px;font-weight:800;font-size:5.4px;line-height:7px;color:var(--orange)}
.body{position:absolute;font-size:4.6px;line-height:6.6px;color:var(--text);text-align:justify;hyphens:auto;-webkit-hyphens:auto}
.body p+p{margin-top:6px}
.label{position:absolute;font-weight:800;font-size:7px;color:var(--navy)}
.portrait{position:absolute;left:357px;top:89px;width:94px;height:65px;background:linear-gradient(180deg,#eceeef,#d6d8da)}
.badge{position:absolute;width:60px;height:60px;border-radius:50%;background:var(--green);border:2px solid #fff;outline:1px solid var(--green)}
.badge svg{position:absolute;left:15px;top:15px}
.calc-note{position:absolute;font-weight:800;font-size:5.4px;line-height:7px;color:var(--orange)}
.bullet{position:absolute;left:358px;width:100px}
.bullet svg{position:absolute;left:0;top:0}
.bullet p{margin-left:14px;font-weight:800;font-size:4.8px;line-height:6.6px;color:var(--navy)}
.step{position:absolute;text-align:center;width:50px;margin-left:-25px;font-weight:800;font-size:4.8px;line-height:6.2px;color:var(--navy)}
.step svg{display:block;margin:0 auto 4px}
.contact{position:absolute;left:253px;top:116px;font-size:4.8px;line-height:9.5px}
.contact li{list-style:none;display:flex;align-items:center;gap:5px}
.office{position:absolute;font-size:4.8px;line-height:7.4px}
.office h4{font-weight:800;font-size:7px;color:var(--navy);line-height:9px;letter-spacing:.5px}
.map{position:absolute;top:196px;width:84px;height:94px;background:linear-gradient(160deg,#c9d3e0,#aebdd2)}
</style>
</head>
<body>

<!-- Seite 1: Übersicht -->
<section class="page col-l row1">
  <div class="kicker">STEUERN<span class="sep"></span>MEHRWERT<span class="sep"></span>TREUHAND<span class="sep"></span></div>
  <div class="photo" role="img" aria-label="Stadtstrasse mit Bürohochhäusern und Bäumen, farbig getönt">
    <div class="brand-name">Varen Treuhand</div>
    <div class="photo-url">varentreuhand.ch</div>
  </div>
  <div class="head" style="top:65px">Zuverlässig und partnerschaftlich:<br>Ihre massgeschneiderten Treuhand-Lösungen</div>
  <div class="body" style="left:253px;top:88px;width:89px">
    <p>Sie möchten Ihre Steuern, Ihre Buchhaltung oder Ihr Lohnwesen in verlässliche Hände geben? Sie legen Wert auf eine persönliche Betreuung mit gleichbleibendem Ansprechpartner, auf individuelle Strategien und auf ein angenehmes Miteinander?</p>
    <p>Dann freue ich mich auf Ihre Kontaktaufnahme.</p>
  </div>
  <div class="portrait" role="img" aria-label="Porträt der Beraterin vor hellem Hintergrund"></div>
  <div class="label" style="left:253px;top:178px">BUCHHALTUNG</div>
  <div class="body" style="left:253px;top:187px;width:89px">Buchhaltung ist komplex und aufwendig – das kostet Unternehmer viel Zeit, die sie anderswo wertschöpfend einsetzen könnten. Mithilfe moderner Hilfsmittel und bewährter Prozesse entlaste ich Sie zuverlässig und zum Fixpreis.</div>
  <div class="label" style="left:358px;top:178px">STEUERERKLÄRUNG</div>
  <div class="body" style="left:358px;top:187px;width:89px">Jeder möchte seine Steuerlast optimieren, nur wenige setzen sich aktiv damit auseinander. Denn das kostet Zeit und verlangt nach umfangreichem Wissen. Vertrauen Sie mir Ihre Steuererklärungen an – und holen Sie sich zurück, was Ihnen zusteht.</div>
  <div class="label" style="left:253px;top:241px">LOHNWESEN</div>
  <div class="body" style="left:253px;top:250px;width:89px">Entscheiden Sie selbst, in welcher Form Sie auf meine Expertise zugreifen, um sich beim Thema Lohnbuchhaltung zu entlasten.</div>
  <div class="label" style="left:358px;top:241px">FIRMENGRÜNDUNG</div>
  <div class="body" style="left:358px;top:250px;width:89px">Gründen Sie Ihre Schweizer Gesellschaft schnell und sicher. Mit meiner langjährigen Erfahrung, meinem Wissen und meiner Zusammenarbeit mit einem versierten Notar unterstütze ich Sie zuverlässig – auch über Ihre Gründung hinaus.</div>
</section>

<!-- Seite 2: Buchhaltung -->
<section class="page col-r row1">
  <div class="kicker">ADDITION<span class="sep"></span>SUBTRAKTION<span class="sep"></span>ERFOLG<span class="sep"></span></div>
  <div class="photo warm" role="img" aria-label="Blick durch Baumkronen auf Glashochhäuser, farbig getönt">
    <div class="photo-word" style="right:6px;top:14px;font-size:48px">buch-<br>haltung</div>
  </div>
  <div class="head" style="top:65px">Buchhaltung kostet Sie viel Zeit<br>– Ich gebe Sie Ihnen zurück</div>
  <div class="sub" style="top:85px">Ich übernehme Ihre Buchhaltung –<br>akribisch, verlässlich, verantwortungsvoll</div>
  <div class="body" style="left:253px;top:113px;width:89px">
    <p>Unternehmer zählen die Buchhaltung in der Regel nicht zu ihren Leidenschaften.</p>
    <p>Und dennoch ist eine ordentliche Buchhaltung das Rückgrat eines jeden erfolgreichen Betriebs. Es ergibt also durchaus Sinn, hierfür ausreichend Ressourcen bereitzustellen – jedoch nicht die eigenen.</p>
    <p>Wenn Sie selbst oder Ihre Mitarbeiter sich um dieses komplexe „Pflichtthema“ kümmern, bleiben andere, wertschöpfende Tätigkeiten auf der Strecke: neue Kunden akquirieren, Produkte weiterentwickeln, Services ausbauen usw.</p>
  </div>
  <div class="body" style="left:358px;top:113px;width:89px">
    <p>Die Folge: Es kommt zu unnötigem Mehraufwand und die Entwicklung Ihres Unternehmens schreitet langsamer voran als geplant.</p>
    <p>Beides ist unschön – und beides lässt sich leicht vermeiden. Nutzen Sie Ihre wertvolle Zeit lieber gewinnbringend und überlassen Sie Ihre Buchhaltung einem Profi.</p>
    <p>Mit viel Erfahrung, Wissen und Leidenschaft kümmere ich mich um Ihre Geschäftsvorfälle, während Ihr Team und Sie sich auf Ihre Kerntätigkeit fokussieren.</p>
  </div>
  <div class="badge" style="left:214px;top:238px">
    <svg width="30" height="30" viewBox="0 0 30 30" fill="none" stroke="#fff" stroke-width="1.8"><rect x="1" y="1" width="28" height="28" rx="3"/><path d="M5 9h7M18 6l5 5M23 6l-5 5M5 21h7M8.5 17.5v7M18 19h6M18 23h6"/></svg>
  </div>
  <div class="calc-note" style="left:284px;top:261px">Mit individuellem Preisrechner auf:<br>www.varentreuhand.ch/treuhand/buchhaltung</div>
</section>

<!-- Seite 3: Lohn -->
<section class="page col-l row2">
  <div class="kicker">BERECHNUNG<span class="sep"></span>PRÄZISION<span class="sep"></span>ENTLASTUNG<span class="sep"></span></div>
  <div class="photo" role="img" aria-label="Moderne Glasfassade mit Bäumen davor, farbig getönt">
    <div class="photo-word" style="right:12px;top:14px;font-size:50px">lohn</div>
  </div>
  <div class="head" style="top:65px">Lohnbuchhaltung ohne Stress:<br>So gewinnen Sie mehr Zeit</div>
  <div class="sub" style="top:86px">Ich erledige Ihr Lohnwesen – präzise, sicher, zuverlässig</div>
  <div class="body" style="left:253px;top:105px;width:89px">
    <p>Sicherlich stimmen Sie mir zu, wenn ich das Personalwesen und die Saläradministration zu den sensiblen Bereichen Ihres Unternehmens zähle. Schliesslich erwarten Ihre Mitarbeiter, dass ihre Gehälter pünktlich auf dem Konto eingehen.</p>
    <p>Doch die Lohnbuchhaltung ist komplex und daher zeitaufwendig – sie bindet wertvolle Ressourcen, die Ihnen für andere, wertschöpfende Tätigkeiten fehlen.</p>
    <p>Holen Sie sich die Zeit zurück und legen Sie Ihre Lohnbuchhaltung in meine Hände. Dabei haben Sie die Wahl zwischen Optimierung und Outsourcing:</p>
  </div>
  <div class="bullet" style="top:104px">
    <svg width="10" height="10" viewBox="0 0 10 10"><circle cx="5" cy="5" r="5" fill="var(--orange)"/><path d="M2.5 5h5M5.5 3l2 2-2 2" stroke="#fff" stroke-width="1" fill="none"/></svg>
    <p>Sie übernehmen die vorbereitenden Arbeiten, während ich mich um die Umsetzung kümmere. So optimieren wir gemeinsam Ihre Vorgänge und entlasten Ihre interne Buchhaltung.</p>
  </div>
  <div class="bullet" style="top:160px">
    <svg width="10" height="10" viewBox="0 0 10 10"><circle cx="5" cy="5" r="5" fill="var(--orange)"/><path d="M2.5 5h5M5.5 3l2 2-2 2" stroke="#fff" stroke-width="1" fill="none"/></svg>
    <p>Sie lagern Ihre Lohnbuchhaltung an mich aus. Insbesondere kleine und mittlere Unternehmen profitieren vom Outsourcing immens, da sie sich von diesem Thema komplett befreien.</p>
  </div>
</section>

<!-- Seite 4: Steuern -->
<section class="page col-r row2">
  <div class="kicker">EFFIZIENZ<span class="sep"></span>SICHERHEIT<span class="sep"></span>GENAU<span class="sep"></span></div>
  <div class="photo" role="img" aria-label="Baumgesäumte Strasse zwischen Bürogebäuden, farbig getönt">
    <div class="photo-word" style="right:10px;top:14px;font-size:46px">steuern</div>
  </div>
  <div class="head" style="top:65px">Professionell und transparent:<br>Ihre Steuererklärung und Steuerberatung</div>
  <div class="sub" style="top:86px">Ich kümmere mich persönlich um Ihre Steuerangelegenheiten</div>
  <div class="body" style="left:253px;top:106px;width:128px">Steuern sind ein sensibles Thema – schliesslich geht es um Ihr Geld. Setzen Sie gleich auf professionelle Unterstützung: Vermeiden Sie teure Fehler, sparen Sie viel Zeit und schonen Sie Ihre Nerven.</div>
  <div class="label" style="left:253px;top:141px">FÜR PRIVATPERSONEN</div>
  <div class="body" style="left:253px;top:150px;width:128px">
    <p>Weshalb ich mir viel Zeit für Sie nehme und Sie individuell betreue? Weil wir mit Konzepten „von der Stange“ bei Ihrer Steuererklärung nicht weit kommen.</p>
    <p>Hingegen habe ich die Abläufe rund um Ihre Steuerberatung standardisiert – um es Ihnen einfach zu machen: Wir tauschen uns per E-Mail, Telefon, Videocall oder per Post aus. So erhalten Sie schnelle Ergebnisse und sparen sich Weg und Kosten für einen persönlichen Termin.</p>
  </div>
  <div class="badge" style="left:214px;top:218px">
    <svg width="30" height="30" viewBox="0 0 30 30" fill="none" stroke="#fff" stroke-width="1.8"><rect x="1" y="1" width="28" height="28" rx="3"/><path d="M5 9h7M18 6l5 5M23 6l-5 5M5 21h7M8.5 17.5v7M18 19h6M18 23h6"/></svg>
  </div>
  <div class="calc-note" style="left:281px;top:243px">Mit individuellem Preisrechner auf:<br>www.varentreuhand.ch</div>
  <div class="step" style="left:430px;top:106px;width:44px;margin-left:-22px">
    <svg width="16" height="19" viewBox="0 0 16 19" fill="none" stroke="var(--orange)" stroke-width="1"><rect x=".5" y=".5" width="15" height="18" rx="1"/><circle cx="8" cy="9.5" r="4"/><path d="M6 9.5l1.5 1.5 2.5-3"/></svg>Checkliste ausfüllen</div>
  <div class="step" style="left:430px;top:149px;width:44px;margin-left:-22px">
    <svg width="16" height="19" viewBox="0 0 16 19" fill="none" stroke="var(--orange)" stroke-width="1"><path d="M3 .5h10v14H3z"/><path d="M5.5 4h5M5.5 7h5M5.5 10h5M.5 14.5h15v4H.5z"/></svg>Unterlagen bereitstellen</div>
  <div class="step" style="left:430px;top:194px;width:44px;margin-left:-22px">
    <svg width="18" height="13" viewBox="0 0 18 13" fill="none" stroke="var(--orange)" stroke-width="1"><rect x=".5" y=".5" width="17" height="12"/><path d="M.5 .5l8.5 7 8.5-7M.5 12.5l6-6M17.5 12.5l-6-6"/></svg>Unterlagen übergeben</div>
  <div class="step" style="left:430px;top:234px;width:44px;margin-left:-22px">
    <svg width="16" height="19" viewBox="0 0 16 19" fill="none" stroke="var(--orange)" stroke-width="1"><path d="M.5 3.5h11v15H.5z"/><path d="M4 .5h11.5v15"/><path d="M3.5 14l5.5-7"/><circle cx="4" cy="8" r="1.3"/><circle cx="8.5" cy="13" r="1.3"/></svg>Meine Arbeit</div>
  <div class="step" style="left:430px;top:278px;width:44px;margin-left:-22px">
    <svg width="16" height="19" viewBox="0 0 16 19" fill="none" stroke="var(--orange)" stroke-width="1"><path d="M.5 .5h10l5 5v13H.5z"/><path d="M8 15V6M4.5 9.5L8 6l3.5 3.5"/></svg>Unterschreiben + Abgeben</div>
</section>

<!-- Seite 5: Gründen -->
<section class="page col-l row3">
  <div class="kicker">SICHER<span class="sep"></span>PERSÖHNLICH<span class="sep"></span>ERFOLGREICH<span class="sep"></span></div>
  <div class="photo" role="img" aria-label="Glasfassade eines Bürogebäudes mit grünem Baum, farbig getönt">
    <div class="photo-word" style="left:20px;top:12px;font-size:46px;text-align:left">gründen</div>
  </div>
  <div class="head" style="top:66px">Professionelle Unternehmens gründung mit System</div>
  <div class="sub" style="top:80px">Varen Treuhand - Ihr kompetenter Partner</div>
  <div class="body" style="left:253px;top:100px;width:89px">Die Gründung des eigenen Unternehmens gehört zu den emotionalsten Erlebnissen in der Karriere. Gut, wenn man hierbei einen verlässlichen Partner hat, der einen kühlen Kopf bewahrt und sich bis ins Detail mit sämtlichen Anforderungen auskennt. Schon seit mehr als 13 Jahren unterstütze ich Start-ups auf ihrem Weg an die Spitze – vom ersten Tag an rund um die Gründung und danach bei der Buchhaltung, im Lohnwesen und bei den Steuern. Was mich dabei auszeichnet, ist mein persönliches Vorgehen: Ich be-</div>
  <div class="body" style="left:358px;top:100px;width:89px">schäftige mich intensiv mit den Gründern und ihrer Idee, berate sie bei der Auswahl der passenden Rechtsform und kümmere mich um sämtliche Formalitäten. Weil ich möchte, dass wir für Sie von Beginn an die richtigen Weichen stellen, gibt es bei mir keine Standardlösungen, sondern stets eine individuelle Herangehensweise. Fokussieren Sie sich auf den besten Start für Ihr Unternehmen – und überlassen Sie mir das Begleitwerk inklusive sämtlicher notarieller Beglaubigungen.</div>
  <div class="label" style="left:253px;top:214px;font-size:7px;letter-spacing:.4px">IN DREI SCHRITTEN ZUR EIGENEN GmbH ODER AG</div>
  <div class="step" style="left:274px;top:233px">
    <svg width="18" height="18" viewBox="0 0 18 18" fill="none" stroke="var(--orange)" stroke-width="1"><circle cx="9" cy="10" r="7.5"/><path d="M7 1h4M9 1v1.5"/><text x="9" y="12.5" font-size="6" text-anchor="middle" fill="var(--orange)" stroke="none" font-family="Mulish,sans-serif">10</text></svg>Datenerfassung in 10min</div>
  <div class="step" style="left:331px;top:233px">
    <svg width="18" height="18" viewBox="0 0 18 18" fill="none" stroke="var(--orange)" stroke-width="1"><path d="M1 6L9 1l8 5zM1.5 17h15M2.5 15h13M4 7.5v6M7.3 7.5v6M10.7 7.5v6M14 7.5v6"/></svg>Geschäftskonto in nur 24h</div>
  <div class="step" style="left:387px;top:233px">
    <svg width="20" height="18" viewBox="0 0 20 18" fill="none" stroke="var(--orange)" stroke-width="1"><rect x="5" y="3" width="14" height="14"/><path d="M1 5l7 5 3-2M8 10l-2 3M12 13h5"/></svg>Notartermin im Handumdrehen</div>
</section>

<!-- Seite 6: Kontakt -->
<section class="page col-r row3">
  <div class="kicker">SICHER<span class="sep"></span>PERSÖHNLICH<span class="sep"></span>ERFOLGREICH<span class="sep"></span></div>
  <div class="photo hands" role="img" aria-label="Händedruck zweier Geschäftsleute, warm getönt">
    <div class="photo-word" style="right:14px;top:14px;font-size:46px">kontakt</div>
  </div>
  <div class="head" style="top:66px">Zuverlässig und partnerschaftlich:<br>Ihre massgeschneiderten Treuhand-Lösungen</div>
  <div class="sub" style="top:88px">Sie haben noch Fragen? Rufen Sie uns an oder senden<br>Sie uns eine Mail, wir helfen Ihnen gerne weiter.</div>
  <ul class="contact">
    <li><svg width="6" height="6" viewBox="0 0 6 6"><path d="M1 0.5l1.3 1.4-.6.8c.4.9 1 1.5 1.8 1.8l.8-.6L5.5 5 4.8 5.7C2.5 5.4.6 3.5.3 1.2z" fill="var(--orange)"/></svg>+41 (0) 41 555 01 20</li>
    <li><svg width="6" height="6" viewBox="0 0 6 6"><rect x="1.3" y="0" width="3.4" height="6" rx=".6" fill="var(--orange)"/><rect x="1.9" y=".8" width="2.2" height="3.8" fill="#fff"/></svg>+41 (0)79 555 02 30 Mobile</li>
    <li><svg width="6" height="6" viewBox="0 0 6 6"><rect x="0" y="1" width="6" height="4" fill="var(--orange)"/><path d="M0 1l3 2.2L6 1" stroke="#fff" stroke-width=".6" fill="none"/></svg>info@varentreuhand.ch</li>
  </ul>
  <div class="office" style="left:253px;top:159px"><h4>LUZERN</h4>Varen Treuhand Consulting GmbH<br>Lindenweg 12<br>6000 Luzern</div>
  <div class="office" style="left:358px;top:159px"><h4>ZÜRICH</h4>Varen Treuhand Consulting GmbH<br>Rebhangweg 8<br>8800 Seeufer</div>
  <div class="map" style="left:254px" role="img" aria-label="Lageplan Standort Luzern"></div>
  <div class="map" style="left:359px" role="img" aria-label="Lageplan Standort Zürich"></div>
</section>

</body>
</html>
```